QDN Advisory needs business card

Having just developed a logo, I now want to use that logo in the development of a business card. The card should contain the logo, my name, title, phone, email, website and physical address. I would like to use one side of the card for details and the other side for logo and messaging. Use your creativity to place the information effectively. I want the logo to appear in a strong blue, which may be matched on the back side of the card, where the logo might be reversed out in white. I want the text to be in either dark blue or black (not light blue or gray).
I am consultant, primarily helping small and mid-size companies refine their strategy, reorganize their staff and propel forward in their industry. I also teach at universities and coach on a one-on-one basis. The final design should reflect expertise, guidance, judgement, perspective, experience.
The font used in the logo is ACaslonPro.

Target Market(s)

small to mid-size companies in the US seeking business guidance

Industry/Entity Type

Business

Font styles to use
Other font styles liked:
• ACaslonPro

Colors
0455a3
0255a3
3277b5

Requirements
Must have
• Card must convey my name and information clearly. Do not make it too small - many of my customers are 50+ years old. Please use all three of my titles: consultant / coach / instructor.
Should not have
• Please do not use icons to represent the phone, email, web. Do not use p / e / w either to indicate those details.

I have decided that a swatch of color, especially a "blue wave," does not work for me. I would rather have a simpler, more reserved look rather than a very contemporary, high color card.

Please do not deconstruct the logo or put it in a different font or italics.

```html
<!DOCTYPE html>
<html lang="en">
<head>
<meta charset="utf-8">
<title>QDN Advisory – Business Card</title>
<link rel="stylesheet" href="https://fonts.googleapis.com/css2?family=Libre+Caslon+Text:wght@400;700&display=swap">
<style>
  :root {
    --brand-blue: #0455a3;
    --brand-blue-deep: #0255a3;
    --brand-blue-soft: #3277b5;
    --ink: #111111;
    --paper: #ffffff;
    --backdrop: #dfe7f0;
  }
  * { margin: 0; padding: 0; box-sizing: border-box; }
  html, body {
    width: 1200px;
    height: 776px;
    overflow: hidden;
    background: var(--backdrop);
    font-family: "Libre Caslon Text", Georgia, serif;
  }
  .sheet {
    position: relative;
    width: 1200px;
    height: 776px;
  }
  .card {
    position: absolute;
    left: 275px;
    width: 650px;
    height: 372px;
    background: var(--paper);
    box-shadow: 0 2px 10px rgba(0, 40, 90, 0.15);
    overflow: hidden;
  }
  .card--front { top: 10px; }
  .card--back  { top: 394px; }

  /* Front: details */
  .identity {
    position: absolute;
    top: 44px;
    left: 0;
    width: 100%;
    text-align: center;
  }
  .identity__name {
    color: var(--brand-blue);
    font-weight: 700;
    font-size: 27px;
    letter-spacing: 0.5px;
    line-height: 1.2;
  }
  .identity__titles {
    color: var(--ink);
    font-size: 32px;
    line-height: 1.3;
    margin-top: 4px;
  }
  .contact-band {
    position: absolute;
    top: 160px;
    left: 0;
    width: 100%;
    height: 155px;
    background: var(--brand-blue);
    color: var(--paper);
    text-align: center;
    padding-top: 34px;
  }
  .contact-band__address {
    font-size: 23px;
    line-height: 1.3;
  }
  .contact-band__reach {
    margin-top: 12px;
    font-weight: 700;
    font-size: 21px;
    white-space: nowrap;
  }
  .contact-band__phone { font-size: 27px; }

  /* Back: name mark and website */
  .brand-mark {
    position: absolute;
    top: 110px;
    left: 0;
    width: 100%;
    text-align: center;
    color: var(--brand-blue);
    font-size: 74px;
    font-weight: 400;
    line-height: 1;
    letter-spacing: 1px;
  }
  .brand-rule {
    position: absolute;
    top: 222px;
    left: 60px;
    width: 530px;
    height: 3px;
    background: var(--brand-blue-soft);
  }
  .website {
    position: absolute;
    top: 272px;
    left: 0;
    width: 100%;
    text-align: center;
    color: var(--ink);
    font-weight: 700;
    font-size: 40px;
  }
</style>
</head>
<body>
  <main class="sheet">
    <section class="card card--front" aria-label="Card front with contact details">
      <div class="identity">
        <p class="identity__name">H. WARREN CASTELLANE, CCIM</p>
        <p class="identity__titles">Consultant - Coach - Instructor</p>
      </div>
      <div class="contact-band">
        <p class="contact-band__address">2417 Larkmoor Court Orlando, FL 32801</p>
        <p class="contact-band__reach"><span class="contact-band__phone">(407) 555-0148</span>&nbsp; - &nbsp;Warren@qdn-advisory.com</p>
      </div>
    </section>

    <section class="card card--back" aria-label="Card back with company name">
      <p class="brand-mark">QDN Advisory</p>
      <div class="brand-rule"></div>
      <p class="website">www.qdn-advisory.com</p>
    </section>
  </main>
</body>
</html>
```